professional business card

A Clean looking business card for a money transfer company. Our company is call Velorix= Transfer + Send = Transcend (next level)
to show professionalism as well as some effects to show digital tech.

1 side to have position, name and address
2 side to have company name and show that we provide money exchange and cross-border money transfer

Target Market(s)

Remittance companies and high net worth individuals

Industry/Entity Type

Finance

Contact Information for Business Card

Name, address, email, title, services- money exchange and cross-border remittance

Requirements
Nice to have
• Digital age feel

```html
<!DOCTYPE html>
<html lang="en">
<head>
<meta charset="utf-8">
<title>Velorix Business Card</title>
<link rel="stylesheet" href="https://fonts.googleapis.com/css2?family=Montserrat:wght@300;400;500;700;800&family=Oswald:wght@500&display=swap">
<style>
  :root {
    --stage: #3a3a3c;
    --card: #0d0d0e;
    --cyan: #6dd6e4;
    --cyan-deep: #2aa9c9;
    --white: #ffffff;
    --coin: #f2b619;
    --arrow-blue: #2f8fdc;
  }
  * { margin: 0; padding: 0; box-sizing: border-box; }
  html, body { width: 1200px; height: 875px; overflow: hidden; }
  body {
    background: var(--stage);
    font-family: "Montserrat", sans-serif;
    position: relative;
  }
  .card {
    position: absolute;
    left: 267px;
    width: 666px;
    height: 380px;
    background: var(--card);
    overflow: hidden;
    box-shadow: 0 18px 40px rgba(0,0,0,0.45);
  }
  .card--front { top: 38px; }
  .card--back { top: 457px; }

  .pattern-field {
    position: absolute;
    top: 0; right: 0;
    width: 56%;
    height: 100%;
    background: linear-gradient(90deg, rgba(109,214,228,0) 0%, rgba(109,214,228,0.25) 30%, rgba(109,214,228,0.7) 65%, var(--cyan) 100%);
  }

  /* Front */
  .brand {
    position: absolute;
    left: 48px; top: 58px;
    display: flex; align-items: center; gap: 16px;
  }
  .brand__mark {
    width: 40px; height: 40px;
    background: var(--cyan);
  }
  .brand__name {
    font-weight: 500;
    font-size: 58px;
    letter-spacing: 5px;
    color: var(--white);
    line-height: 1;
  }
  .services {
    position: absolute;
    left: 50px; top: 138px;
    font-family: "Oswald", sans-serif;
    font-weight: 500;
    font-size: 29px;
    line-height: 1.12;
    color: var(--white);
    text-transform: uppercase;
  }
  .exchange-illustration {
    position: absolute;
    left: 110px; top: 250px;
    width: 110px; height: 110px;
    border-radius: 50%;
    background: radial-gradient(circle at 40% 35%, var(--coin) 0%, var(--coin) 30%, var(--arrow-blue) 60%, rgba(47,143,220,0) 72%);
  }

  /* Back */
  .person {
    position: absolute;
    left: 60px; top: 110px;
    color: var(--white);
  }
  .person__name {
    font-size: 34px;
    letter-spacing: 2px;
    line-height: 1;
  }
  .person__first { font-weight: 800; }
  .person__last { font-weight: 300; }
  .person__title {
    margin-top: 8px;
    font-size: 15px;
    font-weight: 500;
    letter-spacing: 0.5px;
  }
  .person__rule {
    margin-top: 10px;
    width: 270px;
    height: 2px;
    background: var(--white);
    position: relative;
  }
  .person__rule::before {
    content: "";
    position: absolute;
    left: 0; top: 2px;
    width: 46px; height: 5px;
    background: var(--cyan);
  }
  .contact {
    position: absolute;
    left: 60px; top: 232px;
    display: flex;
    gap: 18px;
  }
  .contact__icons {
    width: 30px;
    background: var(--cyan);
    display: flex; flex-direction: column;
    justify-content: space-around; align-items: center;
    padding: 10px 0;
  }
  .contact__icons svg { width: 16px; height: 16px; }
  .contact__list {
    list-style: none;
    color: var(--white);
    font-size: 16px;
    font-weight: 500;
    letter-spacing: 0.4px;
    line-height: 26px;
    padding: 6px 0;
  }
</style>
</head>
<body>

<section class="card card--front">
  <div class="pattern-field" role="img" aria-label="Cyan triangle mosaic fading into black"></div>
  <div class="brand">
    <span class="brand__mark"></span>
    <span class="brand__name">VELORIX</span>
  </div>
  <p class="services">We provide money exchange<br>and cross-border<br>money transfer</p>
  <div class="exchange-illustration" role="img" aria-label="Two gold coins with dollar and rupee signs circled by blue exchange arrows"></div>
</section>

<section class="card card--back">
  <div class="pattern-field" role="img" aria-label="Cyan triangle mosaic fading into black"></div>
  <div class="person">
    <p class="person__name"><span class="person__first">DANIEL</span> <span class="person__last">REYES</span></p>
    <p class="person__title">Co-Founder Brand Name</p>
    <div class="person__rule"></div>
  </div>
  <div class="contact">
    <div class="contact__icons">
      <svg viewBox="0 0 16 16" aria-label="Address"><path d="M8 1a5 5 0 0 0-5 5c0 3.5 5 9 5 9s5-5.5 5-9a5 5 0 0 0-5-5zm0 7a2 2 0 1 1 0-4 2 2 0 0 1 0 4z" fill="#0d0d0e"/></svg>
      <svg viewBox="0 0 16 16" aria-label="Phone"><path d="M4 1l2.5 3-1.5 2a9 9 0 0 0 5 5l2-1.5 3 2.5-1.5 2.5C7 14 2 9 1.5 2.5z" fill="#0d0d0e"/></svg>
      <svg viewBox="0 0 16 16" aria-label="Email"><path d="M1 3h14v10H1z" fill="#0d0d0e"/><path d="M1 3l7 6 7-6" stroke="#6dd6e4" stroke-width="1.3" fill="none"/></svg>
      <svg viewBox="0 0 16 16" aria-label="Website"><path d="M3 1l10 7-4.5 1 2.5 5-2 1-2.5-5L3 13z" fill="#0d0d0e"/></svg>
    </div>
    <ul class="contact__list">
      <li>123 Dummy, Lorem Ipsum</li>
      <li>+00 1234 5XXX 9012</li>
      <li>info@email space</li>
      <li>www websiteaddress</li>
    </ul>
  </div>
</section>

</body>
</html>
```